TIVARELCAP web-presence redisign

We would like to have our existing web-presence redesigned. Have a look at www.tivarel.ch (please use explorer). To the existing 11 pages we would add one more.

```html
<!DOCTYPE html>
<html lang="de">
<head>
<meta charset="utf-8">
<title>TIVARELCAP Zahnarztpraxis</title>
<link rel="stylesheet" href="https://fonts.googleapis.com/css2?family=Ubuntu:wght@400;500&family=Oswald:wght@300&display=swap">
<style>
  :root {
    --top-strip: #a3a3a3;
    --header-bg: #cdcdcd;
    --orange: #e6b04c;
    --orange-bright: #f6b431;
    --orange-deep: #d59a2c;
    --light-bg: #f0f0f0;
    --text-dark: #4a4a4a;
    --text-brown: #5b4520;
    --white: #ffffff;
    --icon-dark: #1f1f1f;
  }
  * { box-sizing: border-box; margin: 0; padding: 0; }
  html, body { width: 927px; height: 1200px; overflow: hidden; }
  body { position: relative; background: var(--white); font-family: 'Ubuntu', sans-serif; color: var(--text-dark); }

  .site-header { position: absolute; left: 0; top: 0; width: 927px; height: 314px; background: var(--header-bg); border-top: 7px solid var(--top-strip); }
  .brand { position: absolute; left: 104px; top: 40px; display: flex; align-items: center; gap: 14px; }
  .brand-mark { width: 64px; height: 64px; border-radius: 50%; background: var(--orange-bright); flex: none; }
  .brand-name { font-size: 31px; font-weight: 400; color: var(--white); line-height: 1.05; letter-spacing: 1px; }
  .brand-name span { display: block; font-size: 27px; letter-spacing: 0; }
  .header-rule { position: absolute; left: 88px; top: 151px; width: 720px; height: 2px; background: linear-gradient(90deg, rgba(255,255,255,0), #fff 50%, rgba(255,255,255,0)); }
  .contact { position: absolute; left: 660px; top: 31px; font-size: 13.5px; line-height: 17px; color: #555; }
  .contact p + p { margin-top: 9px; }

  .main-nav { position: absolute; top: 240px; left: 217px; display: flex; align-items: center; font-size: 12.5px; color: var(--white); }
  .main-nav a { color: var(--white); text-decoration: none; }
  .main-nav .active { background: var(--orange-bright); width: 75px; height: 27px; line-height: 27px; text-align: center; margin-right: 27px; }
  .main-nav .sep { margin: 0 24px; }

  .hero { position: absolute; left: 0; top: 314px; width: 927px; height: 430px; background: var(--orange); }
  .hero-title { position: absolute; left: 90px; top: 66px; font-size: 26px; font-weight: 500; line-height: 24px; color: var(--white); }
  .hero-text { position: absolute; left: 92px; top: 148px; width: 372px; font-size: 11.5px; line-height: 24px; color: var(--text-brown); }
  .hero-text p + p { margin-top: 24px; }
  .hero-photo { position: absolute; left: 478px; top: 38px; width: 362px; height: 362px; border-radius: 50%; border: 6px solid var(--orange-deep); background: radial-gradient(circle at 55% 45%, #e9b59a, #c77f5c 55%, #8a5a3e); }

  .welcome { position: absolute; left: 0; top: 744px; width: 927px; height: 312px; background: var(--light-bg); }
  .welcome-title { position: absolute; left: 94px; top: 38px; font-family: 'Oswald', sans-serif; font-weight: 300; font-size: 30px; color: #444; }
  .welcome-rule { position: absolute; left: 94px; top: 87px; width: 478px; height: 2px; background: linear-gradient(90deg, #bdbdbd, rgba(189,189,189,0)); }
  .welcome-text { position: absolute; left: 94px; top: 108px; width: 460px; font-size: 11px; line-height: 20px; color: #555; }
  .welcome-text p + p { margin-top: 18px; }

  .site-footer { position: absolute; left: 0; top: 1056px; width: 927px; height: 144px; background: var(--orange); text-align: center; }
  .social { position: absolute; top: 20px; left: 319px; display: flex; gap: 7px; list-style: none; }
  .social li { width: 22px; height: 22px; border-radius: 50%; background: var(--icon-dark); }
  .footer-nav { position: absolute; top: 56px; left: 0; width: 927px; font-size: 11px; color: var(--icon-dark); }
  .footer-nav a { color: var(--icon-dark); text-decoration: none; }
  .footer-nav .sep { margin: 0 24px; }
  .copyright { position: absolute; top: 81px; left: 0; width: 927px; font-size: 11.5px; line-height: 16px; color: #fbe8c4; }
</style>
</head>
<body>
  <header class="site-header">
    <div class="brand">
      <div class="brand-mark"></div>
      <div class="brand-name">TIVARELCAP<span>Zahnarztpraxis</span></div>
    </div>
    <div class="header-rule"></div>
    <address class="contact" style="font-style:normal">
      <p>Mattenstrasse 14<br>CH-8400 Winterthur</p>
      <p>T: +41 (0)44 555 01 23<br>info@tivarel.ch</p>
    </address>
    <nav class="main-nav">
      <a class="active" href="#">Home</a>
      <a href="#">Zahnmedizin</a><span class="sep">|</span>
      <a href="#">Dentalhygiene</a><span class="sep">|</span>
      <a href="#">Team</a><span class="sep">|</span>
      <a href="#">Kontakt</a>
    </nav>
  </header>

  <section class="hero">
    <h1 class="hero-title">Lorem ipsum dolor sit amet,<br>consectetuer .</h1>
    <div class="hero-text">
      <p>Lorem ipsum dolor sit amet, consectetuer adipiscing elit. Donec odio. Quisque volutpat mattis eros. Nullam malesuada erat ut turpis. Suspendisse urna nibh, viverra non, semper suscipit, posuere a, pede.</p>
      <p>Donec nec justo eget felis facilisis fermentum. Aliquam porttitor mauris sit amet orci. Aenean dignissim pellentesque felis.</p>
    </div>
    <div class="hero-photo" role="img" aria-label="Portrait photo of the dentist"></div>
  </section>

  <section class="welcome">
    <h2 class="welcome-title">Herzlich willkommen in unserer neuen Praxis.</h2>
    <div class="welcome-rule"></div>
    <div class="welcome-text">
      <p>Es ist unser Ziel, Ihr Wohlbefinden zu steigern. Sie sollen die Schönheit des Alltags mit gesunden Zähnen geniessen und in jeder Situation herzhaft lachen können.</p>
      <p>Ihre Zahnärztin</p>
      <p>Dr. med. dent. Lena Marti-Keller</p>
    </div>
  </section>

  <footer class="site-footer">
    <ul class="social" aria-label="Social media">
      <li></li><li></li><li></li><li></li><li></li><li></li><li></li><li></li><li></li><li></li>
    </ul>
    <nav class="footer-nav">
      <a href="#">Home</a><span class="sep">|</span>
      <a href="#">Zahnmedizin</a><span class="sep">|</span>
      <a href="#">Dentalhygiene</a><span class="sep">|</span>
      <a href="#">Team</a><span class="sep">|</span>
      <a href="#">Kontakt</a>
    </nav>
    <p class="copyright">Copyright 2007 © TIVARELCAP | Dr. med. dent. L. Marti-Keller.<br>All rights reserved. Privacy Policy</p>
  </footer>
</body>
</html>
```